Life Coaching Business Card

Please check out my website at www.lorettavanmeer.example. Ideally I would like to use the same colors that I used on the site to match my business cards i.e: pink, green, teal, white
I want the final design to include a picture of me and also to be appealing and eye catching. For the picture I submitted, you can crop it smaller to just have my face (exclude my chest) showing.
Industry/Entity Type
Business
Contact Information for Business Card
Loretta Vanmeer
Transformational Life Coach
web: www.lorettavanmeer.example
email: loretta@lorettavanmeer.example
Phone: 555-318-4072
Look and feel
Each slider illustrates characteristics of the customer's brand and the style your logo design should communicate.

```html
<!DOCTYPE html>
<html lang="en">
<head>
<meta charset="utf-8">
<title>Loretta Vanmeer – Business Card</title>
<link rel="stylesheet" href="https://fonts.googleapis.com/css2?family=Jura:wght@500;600&family=Russo+One&display=swap">
<style>
  :root {
    --lime: #aaff00;
    --pink: #ff14e8;
    --teal: #5ef5ea;
    --white: #ffffff;
    --paper-light: #ffffff;
    --paper-shade: #e9e9e9;
    --ink: #111111;
    --photo-dark: #2b2b2b;
    --photo-light: #bdbdbd;
  }
  html, body {
    margin: 0;
    padding: 0;
    width: 1200px;
    height: 686px;
    overflow: hidden;
    background: var(--white);
  }
  .card {
    position: relative;
    width: 1200px;
    height: 686px;
    overflow: hidden;
    background: linear-gradient(200deg, var(--paper-light) 0%, var(--paper-light) 40%, var(--paper-shade) 100%);
    font-family: "Jura", sans-serif;
  }
  .brand-panel {
    position: absolute;
    left: 0;
    top: 0;
    width: 642px;
    height: 686px;
    background: var(--lime);
  }
  .portrait {
    position: absolute;
    left: 96px;
    top: 82px;
    width: 366px;
    height: 366px;
    border-radius: 50%;
    background: radial-gradient(circle at 50% 45%, var(--photo-light) 0%, #7a7a7a 55%, var(--photo-dark) 100%);
    box-shadow: 0 6px 14px rgba(0,0,0,0.35);
  }
  .swatches {
    position: absolute;
    top: 64px;
    left: 714px;
    display: flex;
    gap: 29px;
  }
  .swatch {
    width: 96px;
    height: 96px;
    border-radius: 50%;
  }
  .swatch--lime { background: var(--lime); }
  .swatch--pink { background: var(--pink); }
  .swatch--teal { background: var(--teal); }
  .contact {
    position: absolute;
    left: 560px;
    height: 97px;
    width: 217px;
    border-radius: 48px 0 0 48px;
    background: linear-gradient(90deg, var(--white) 70%, rgba(255,255,255,0) 100%);
  }
  .contact--phone { top: 214px; }
  .contact--web { top: 375px; }
  .contact--email { top: 536px; }
  .contact__icon {
    position: absolute;
    left: 26px;
    top: 28px;
    width: 42px;
    height: 42px;
  }
  .contact__text {
    position: absolute;
    left: 112px;
    top: 50%;
    transform: translateY(-50%);
    white-space: nowrap;
    color: var(--ink);
    font-weight: 600;
    letter-spacing: 0.3px;
    text-transform: uppercase;
  }
  .contact--phone .contact__text { font-size: 26px; left: 110px; }
  .contact--phone .contact__digits { font-size: 31px; }
  .contact--web .contact__text { font-size: 21px; left: 118px; }
  .contact--email .contact__text { font-size: 20px; left: 124px; }
  .cap-big { font-size: 1.25em; }
  .identity {
    position: absolute;
    left: 54px;
    top: 540px;
  }
  .identity__name {
    margin: 0;
    font-family: "Russo One", sans-serif;
    font-weight: 400;
    text-transform: uppercase;
    font-size: 33px;
    line-height: 44px;
    color: var(--ink);
    letter-spacing: 1.5px;
  }
  .identity__rule {
    width: 398px;
    height: 1px;
    margin: 10px 0 10px;
    background: var(--white);
  }
  .identity__title {
    margin: 0;
    font-family: "Jura", sans-serif;
    font-weight: 500;
    text-transform: uppercase;
    font-size: 22px;
    line-height: 34px;
    color: var(--white);
    letter-spacing: 1px;
  }
  .accent-bar {
    position: absolute;
    left: 872px;
    top: 634px;
    display: flex;
    height: 52px;
  }
  .accent-bar__pink { width: 95px; background: var(--pink); }
  .accent-bar__teal { width: 96px; background: var(--teal); border-radius: 0 26px 26px 0; }
</style>
</head>
<body>
<main class="card">
  <div class="brand-panel"></div>
  <div class="portrait" role="img" aria-label="Black and white portrait of Loretta Vanmeer"></div>

  <div class="swatches">
    <span class="swatch swatch--lime"></span>
    <span class="swatch swatch--pink"></span>
    <span class="swatch swatch--teal"></span>
  </div>

  <div class="contact contact--phone">
    <svg class="contact__icon" viewBox="0 0 24 24" aria-hidden="true">
      <path fill="#111" d="M6.6 2.5c.6-.4 1.3-.2 1.7.4l1.8 3.1c.3.6.2 1.3-.3 1.7L8.5 8.8c-.3.3-.4.7-.2 1.1 1.1 2.3 2.9 4.4 5 5.9.4.3.9.2 1.2-.1l1.1-1.2c.5-.5 1.2-.6 1.7-.2l3 2c.6.4.8 1.2.4 1.8l-1.2 1.9c-.6.9-1.7 1.4-2.8 1.1C10.9 19.5 4.8 12.9 3.4 6.6c-.2-1 .2-2 1.1-2.6z"/>
    </svg>
    <span class="contact__text"><span class="cap-big">P</span>hone: <span class="contact__digits">555-318-4072</span></span>
  </div>

  <div class="contact contact--web">
    <svg class="contact__icon" viewBox="0 0 24 24" aria-hidden="true">
      <circle cx="12" cy="12" r="10" fill="#111"/>
      <g fill="none" stroke="#fff" stroke-width="1.3">
        <ellipse cx="12" cy="12" rx="4.2" ry="10"/>
        <line x1="12" y1="2" x2="12" y2="22"/>
        <line x1="2" y1="12" x2="22" y2="12"/>
        <line x1="3.5" y1="7" x2="20.5" y2="7"/>
        <line x1="3.5" y1="17" x2="20.5" y2="17"/>
      </g>
    </svg>
    <span class="contact__text">web: www.lorettavanmeer.example</span>
  </div>

  <div class="contact contact--email">
    <svg class="contact__icon" viewBox="0 0 24 24" aria-hidden="true">
      <rect x="1" y="4.5" width="22" height="15" fill="#111"/>
      <path d="M1.5 5l10.5 8.5L22.5 5M1.5 19l8-7M22.5 19l-8-7" fill="none" stroke="#fff" stroke-width="1.2"/>
    </svg>
    <span class="contact__text">email: loretta@lorettavanmeer.example</span>
  </div>

  <div class="identity">
    <h1 class="identity__name"><span class="cap-big">L</span>oretta <span class="cap-big">V</span>anmeer</h1>
    <div class="identity__rule"></div>
    <p class="identity__title"><span class="cap-big">T</span>ransformational <span class="cap-big">L</span>ife <span class="cap-big">C</span>oach</p>
  </div>

  <div class="accent-bar">
    <span class="accent-bar__pink"></span>
    <span class="accent-bar__teal"></span>
  </div>
</main>
</body>
</html>
```